Eye catching new brochure to intriduce our new service.

Harbour Bright Works has recently acquired a building license. We have been electrical contractors since 2008 and are adding a building license to our company. This will enable us to carry out a wide variety of additional services.
We need a flyer A4 (email), A5, chatterbox flyer. to reach existing customers to inform them of our new license an to also reach new customers.

Target Market(s)

Residential home owners, renovators, people relocating offfice,warehouse spaces.

Industry/Entity Type

Electrical

Font styles to use
Sans Serif

Requirements
Must have
• Company logo - still being designed.
• Guild of Framers logo
• Tolv logo
• Accepts Pexo/Cardwise + logo
• Photos down one side in order top 560,586,637,662,230
• P 1300 738 614
• E info@harbourbrightworks.com.au
• w www.harbourbrightworks.com.au
Nice to have
• "Builders & Electricians"
Should not have
• Fluoro colours

```html
<!DOCTYPE html>
<html lang="en">
<head>
<meta charset="utf-8">
<title>Harbour Bright Works – Building &amp; Electrical Flyer</title>
<link rel="stylesheet" href="https://fonts.googleapis.com/css2?family=Montserrat:wght@600;700&family=Questrial&display=swap">
<style>
  :root {
    --stage: #e9ebee;
    --paper: #ffffff;
    --navy: #163c60;
    --blue: #1f6aa0;
    --sky: #5aa7d4;
    --ice: #d6e9f5;
    --ink: #4e555c;
    --muted: #8a9198;
  }
  * { box-sizing: border-box; margin: 0; padding: 0; }
  html, body { width: 1200px; height: 867px; overflow: hidden; }
  body {
    background: var(--stage);
    font-family: "Questrial", "Century Gothic", sans-serif;
    color: var(--ink);
  }
  .flyer {
    position: absolute;
    left: 300px; top: 9px;
    width: 600px; height: 848px;
    background: var(--paper);
    box-shadow: 0 6px 24px rgba(0,0,0,.18);
    overflow: hidden;
  }
  .flyer-art { position: absolute; left: 0; top: 0; width: 600px; height: 520px; display: block; }
  .brand { position: absolute; left: 14px; top: 14px; width: 140px; }
  .brand-name {
    font-family: "Montserrat", sans-serif; font-weight: 700;
    font-size: 17px; line-height: 1.05; color: var(--blue);
  }
  .brand-tag {
    margin-top: 5px; font-size: 9px; letter-spacing: .12em;
    color: var(--navy); text-transform: uppercase;
  }
  .about { position: absolute; left: 46px; top: 524px; width: 512px; }
  .about-title {
    font-family: "Montserrat", sans-serif; font-weight: 700;
    font-size: 20px; line-height: 1.2; color: var(--navy); margin-bottom: 8px;
  }
  .about p { font-size: 12px; line-height: 1.4; margin-bottom: 5px; }
  .about .licence-news {
    font-family: "Montserrat", sans-serif; font-weight: 600;
    font-size: 12px; color: var(--blue); margin-bottom: 7px;
  }
  .credentials {
    position: absolute; left: 40px; right: 40px; top: 738px;
    display: flex; justify-content: space-between; align-items: center;
  }
  .guild { display: flex; align-items: center; gap: 8px; }
  .seal {
    width: 38px; height: 38px; border-radius: 50%;
    background: var(--ice); border: 2px solid var(--navy);
  }
  .guild-name {
    font-family: "Montserrat", sans-serif; font-weight: 700;
    font-size: 12px; line-height: 1.15; color: var(--navy);
  }
  .member { display: flex; flex-direction: column; align-items: center; gap: 3px; }
  .member .seal { width: 44px; height: 44px; background: #f3f5f7; border-color: var(--muted); }
  .member-name { font-size: 10px; color: var(--muted); letter-spacing: .1em; }
  .payments { text-align: center; }
  .payments-label {
    background: var(--navy); color: #fff; font-size: 7.5px;
    letter-spacing: .06em; text-transform: uppercase; padding: 3px 6px; margin-bottom: 5px;
  }
  .cards { display: flex; gap: 6px; justify-content: center; }
  .card {
    width: 62px; height: 28px; border: 1px solid #c4cad0; background: #fff;
    display: flex; align-items: center; justify-content: center;
    font-family: "Montserrat", sans-serif; font-weight: 700; font-size: 10px; color: var(--navy);
  }
  .footer-band { position: absolute; left: 0; bottom: 0; width: 600px; height: 48px; display: block; }
  .contact {
    position: absolute; left: 0; right: 0; bottom: 7px;
    display: flex; justify-content: center; gap: 22px;
    font-size: 11px; color: #fff; letter-spacing: .02em;
  }
  .contact b { font-family: "Montserrat", sans-serif; font-weight: 700; margin-right: 4px; }
</style>
</head>
<body>
<main class="flyer">
  <svg class="flyer-art" viewBox="0 0 600 520" xmlns="http://www.w3.org/2000/svg">
    <defs>
      <linearGradient id="heroTone" x1="0" y1="0" x2="0" y2="1">
        <stop offset="0" stop-color="#5f9fd6"/>
        <stop offset=".45" stop-color="#c7a690"/>
        <stop offset="1" stop-color="#e6e2da"/>
      </linearGradient>
      <linearGradient id="toneGrey" x1="0" y1="0" x2="1" y2="1"><stop offset="0" stop-color="#9aa3a8"/><stop offset="1" stop-color="#d8d6d0"/></linearGradient>
      <linearGradient id="toneOrange" x1="0" y1="0" x2="0" y2="1"><stop offset="0" stop-color="#d8833e"/><stop offset="1" stop-color="#c9c9c5"/></linearGradient>
      <linearGradient id="toneHouse" x1="0" y1="0" x2="0" y2="1"><stop offset="0" stop-color="#cfd4d3"/><stop offset="1" stop-color="#4a3a2c"/></linearGradient>
      <linearGradient id="toneYard" x1="0" y1="0" x2="0" y2="1"><stop offset="0" stop-color="#8fb3d6"/><stop offset=".5" stop-color="#a2553e"/><stop offset="1" stop-color="#d9c46a"/></linearGradient>
      <linearGradient id="bandBlue" x1="0" y1="0" x2="1" y2="0"><stop offset="0" stop-color="var(--navy)"/><stop offset=".5" stop-color="var(--sky)"/><stop offset="1" stop-color="var(--navy)"/></linearGradient>
      <clipPath id="rowClip"><path d="M0 350 L285 316 L600 346 L600 505 L0 470 Z"/></clipPath>
    </defs>

    <rect class="hero-photo" role="img" aria-label="Photo of a house extension under construction, steel frame and tarps against blue sky" x="0" y="0" width="600" height="352" fill="url(#heroTone)"/>
    <path class="logo-tab" d="M0 0 H170 V70 L150 98 H0 Z" fill="var(--paper)"/>
    <path d="M170 0 V70 L150 98" fill="none" stroke="var(--blue)" stroke-width="4"/>

    <g class="photo-row" clip-path="url(#rowClip)">
      <rect role="img" aria-label="Photo of an opened wall with exposed brickwork" x="0" y="310" width="140" height="200" fill="url(#toneGrey)"/>
      <rect role="img" aria-label="Photo of workers laying a concrete slab" x="144" y="310" width="146" height="200" fill="url(#toneOrange)"/>
      <rect role="img" aria-label="Photo of a rendered house wall with framing below" x="294" y="310" width="146" height="200" fill="url(#toneHouse)"/>
      <rect role="img" aria-label="Photo of a tiled roofline over a backyard" x="444" y="310" width="156" height="200" fill="url(#toneYard)"/>
    </g>
    <path class="chevron-band" d="M0 340 L285 306 L600 336 L600 352 L285 322 L0 356 Z" fill="url(#bandBlue)"/>
    <path d="M0 470 L600 505" stroke="var(--blue)" stroke-width="5"/>
    <path d="M0 478 L600 514" stroke="var(--ice)" stroke-width="3"/>
  </svg>

  <header class="brand">
    <div class="brand-name">Harbour Bright Works</div>
    <div class="brand-tag">Building &amp; Electrical</div>
  </header>

  <section class="about">
    <h1 class="about-title">Who We are:</h1>
    <p class="licence-news">Now licensed builders – Builders &amp; Electricians under one roof.</p>
    <p>Harbour Bright Works provide a fresh, dynamic approach to Building &amp; Electrical Contracting with its focus on servicing the Sydney residential and commercial market.</p>
    <p>Established in 2008, Harbour Bright Works is growing to become one of Sydney’s most reputable Contracting businesses.</p>
    <p>We believe that the success of any business lies in customer satisfaction.</p>
    <p>Harbour Bright Works’s driving force is to offer customers the full professional building &amp; electrical service they deserve.</p>
  </section>

  <section class="credentials">
    <div class="guild">
      <span class="seal"></span>
      <span class="guild-name">Guild of<br>Framers</span>
    </div>
    <div class="member">
      <span class="seal"></span>
      <span class="member-name">Tolv</span>
    </div>
    <div class="payments">
      <div class="payments-label">We accept these major credit cards</div>
      <div class="cards">
        <span class="card">Cardwise</span>
        <span class="card">Pexo</span>
      </div>
    </div>
  </section>

  <svg class="footer-band" viewBox="0 0 600 48" xmlns="http://www.w3.org/2000/svg" preserveAspectRatio="none">
    <defs>
      <linearGradient id="footBlue" x1="0" y1="0" x2="1" y2="0"><stop offset="0" stop-color="var(--navy)"/><stop offset=".6" stop-color="var(--blue)"/><stop offset="1" stop-color="var(--sky)"/></linearGradient>
    </defs>
    <path d="M0 12 Q300 0 600 8" fill="none" stroke="var(--sky)" stroke-width="2"/>
    <path d="M0 20 Q300 8 600 16 V48 H0 Z" fill="url(#footBlue)"/>
  </svg>
  <footer class="contact">
    <span><b>P</b>1300 738 614</span>
    <span><b>E</b>info@harbourbrightworks.com.au</span>
    <span><b>W</b>www.harbourbrightworks.com.au</span>
  </footer>
</main>
</body>
</html>
```